Ribbon Cutting Ceremony Invitation for Solar Company

Need 8.5 x 11 Ribbon Cutting Invitation Design to be used for digital and print. The design should be professional yet creative. It should showcase the theme of a ribbon cutting with some sort of style resembling solar energy. There could also be an option to include a placeholder for a photo of the facility, but that is up to your creative direction. Thanks designers!

Words that should be on it are below:

RIBBON CUTTING CEREMONY

WE FORMALLY INVITE YOU TO THE RIBBON CUTTING EVENT FOR THE NEW SOLAR SYSTEM @ SEABRAMBLE HOTEL AND RESORT.

DATE AND TIME

Use this logo in one of the corners: https://files.plenvarq-media.net/assets/k/kd/Vexa_Energy.png - Let me know if you need it in a different version, transparent, or all white.

PLEASE ASK ME ANY QUESTIONS!!!

Target Market(s)

Business Owners and Executives

Colors

Designer to choose colors to be used in the design.

Requirements
Must have
• Professional design with ribbon cutting and solar theme.

```html
<!DOCTYPE html>
<html lang="en">
<head>
<meta charset="UTF-8">
<title>Ribbon Cutting Ceremony Invitation</title>
<link rel="stylesheet" href="https://fonts.googleapis.com/css2?family=Josefin+Sans:wght@400&family=Montserrat:wght@400;500;800&display=swap">
<style>
  :root {
    --backdrop: #5a5a5a;
    --card-black: #0d0d0d;
    --card-charcoal: #1b1b1b;
    --gold: #e8a81c;
    --gold-light: #f3c64a;
    --ribbon-red: #d01419;
    --ribbon-deep: #6e080b;
    --text-white: #f2f2f2;
  }
  * { box-sizing: border-box; margin: 0; padding: 0; }
  html, body {
    width: 698px; height: 1200px; overflow: hidden;
    background: var(--backdrop);
  }
  .invitation {
    position: absolute; left: 98px; top: 186px;
    width: 502px; height: 712px;
    background: radial-gradient(ellipse at 50% 40%, var(--card-charcoal), var(--card-black) 75%);
    color: var(--text-white);
    font-family: "Montserrat", sans-serif;
    overflow: hidden;
  }
  .brand {
    position: absolute; top: 38px; left: 0; width: 100%;
    text-align: center;
    font-family: "Montserrat", sans-serif; font-weight: 800;
    font-size: 30px; line-height: 40px; color: var(--text-white);
  }
  .title {
    position: absolute; top: 150px; left: 0; width: 100%;
    text-align: center;
    font-family: "Josefin Sans", sans-serif; font-weight: 400;
    font-size: 40px; line-height: 50px; color: var(--gold);
    letter-spacing: 0.5px;
  }
  .ribbon-area {
    position: absolute; top: 262px; left: 0; width: 100%; height: 176px;
    background: linear-gradient(180deg, var(--card-black) 0%, var(--ribbon-deep) 22%, var(--ribbon-red) 45%, var(--ribbon-deep) 75%, var(--card-black) 100%);
  }
  .invite-line {
    position: absolute; top: 495px; left: 0; width: 100%;
    text-align: center; font-size: 13.5px; font-weight: 400;
    letter-spacing: 0.2px;
  }
  .event-name {
    position: absolute; top: 522px; left: 0; width: 100%;
    text-align: center; font-size: 27px; font-weight: 800;
    color: var(--gold-light); letter-spacing: 1px;
  }
  .venue {
    position: absolute; top: 560px; left: 0; width: 100%;
    text-align: center; font-size: 13.5px; font-weight: 400;
  }
  .details {
    position: absolute; left: 42px; top: 614px;
    font-size: 15px; font-weight: 500; list-style: none;
  }
  .details li { height: 36px; }
</style>
</head>
<body>
  <main class="invitation">
    <header class="brand">Vexa Energy</header>

    <h1 class="title">RIBBON CUTTING<br>CEREMONY</h1>

    <div class="ribbon-area" role="img" aria-label="Red satin ribbon tied in a bow, being cut by gold scissors"></div>

    <p class="invite-line">WE FORMALLY INVITE YOU TO THE RIBBON CUTTING EVENT FOR</p>
    <h2 class="event-name">THE NEW SOLAR SYSTEM</h2>
    <p class="venue">@ SEABRAMBLE HOTEL AND RESORT.</p>

    <ul class="details">
      <li>DATE :</li>
      <li>TIME:</li>
    </ul>
  </main>
</body>
</html>
```